Checkout sign

Wall sign for clinic checkout.
“The Good Lord does ALL the healing..
But we DO collect the co-pay”

Add Celtic cross at top and our logo on bottom

```html
<!DOCTYPE html>
<html lang="en">
<head>
<meta charset="utf-8">
<title>Checkout Sign – Kinsella Orthopedic Clinic</title>
<link rel="stylesheet" href="https://fonts.googleapis.com/css2?family=Alegreya:wght@400;800&display=swap">
<style>
  :root {
    --indigo: #1c0a8c;
    --lavender: #978bcd;
    --lavender-pale: #e4e0f3;
    --white: #ffffff;
  }
  html, body {
    margin: 0;
    padding: 0;
    width: 1200px;
    height: 720px;
    overflow: hidden;
    background: var(--white);
  }
  .sign {
    position: relative;
    width: 1200px;
    height: 720px;
    overflow: hidden;
    background: var(--white);
  }
  .sign__backdrop {
    position: absolute;
    inset: 0;
  }
  .sign__message {
    position: absolute;
    left: 0;
    top: 378px;
    width: 1200px;
    margin: 0;
    font-family: "Alegreya", Georgia, serif;
    font-weight: 800;
    color: var(--white);
    font-size: 44px;
    line-height: 74px;
  }
  .sign__line {
    display: block;
    white-space: nowrap;
  }
  .sign__line--first { padding-left: 160px; }
  .sign__line--second { padding-left: 282px; }
  .sign__emphasis { font-size: 58px; }
  .brand {
    position: absolute;
    left: 270px;
    top: 560px;
    font-family: "Alegreya", Georgia, serif;
    font-weight: 400;
    color: var(--indigo);
    text-transform: uppercase;
  }
  .brand__name {
    display: block;
    font-size: 60px;
    line-height: 62px;
    letter-spacing: 1px;
  }
  .brand__descriptor {
    display: block;
    font-size: 27px;
    line-height: 34px;
    letter-spacing: 2px;
    padding-left: 24px;
  }
</style>
</head>
<body>
<main class="sign">
  <svg class="sign__backdrop" width="1200" height="720" viewBox="0 0 1200 720" aria-hidden="false">
    <defs>
      <linearGradient id="cross-fill" x1="0" y1="0" x2="0" y2="1">
        <stop offset="0" stop-color="#3a28a0"/>
        <stop offset="1" stop-color="#6a5cbc"/>
      </linearGradient>
    </defs>
    <!-- indigo field with sweeping top edge -->
    <path class="wave-field" fill="var(--indigo)"
      d="M0,38 C260,40 470,150 680,240 C860,318 1040,338 1200,326 L1200,548 L0,548 Z"/>
    <!-- lavender swoosh bands -->
    <path fill="var(--lavender)"
      d="M0,0 L120,0 C380,10 520,120 700,205 C880,290 1050,290 1200,200 L1200,250 C1050,330 880,330 700,255 C510,175 330,60 0,50 Z"/>
    <path fill="var(--white)"
      d="M0,46 C320,52 500,150 700,235 C880,312 1050,320 1200,238 L1200,248 C1050,330 880,322 700,245 C500,160 320,62 0,56 Z"/>
    <path fill="var(--lavender)"
      d="M300,0 L360,0 C520,40 620,140 780,210 C930,272 1080,250 1200,170 L1200,185 C1080,268 930,290 780,228 C610,160 500,50 300,0 Z"/>
    <path fill="var(--indigo)"
      d="M230,0 L290,0 C460,30 580,150 760,230 C920,300 1070,300 1200,250 L1200,268 C1070,320 910,320 750,250 C570,170 430,40 230,0 Z"/>
    <!-- cross artwork area -->
    <rect x="958" y="78" width="184" height="258" rx="14" fill="url(#cross-fill)"
      role="img" aria-label="Celtic cross with knotwork, indigo on white"/>
    <!-- footer strip -->
    <rect x="0" y="666" width="1200" height="54" fill="var(--lavender)"/>
    <!-- brand mark circle -->
    <circle cx="150" cy="614" r="92" fill="var(--white)" stroke="var(--indigo)" stroke-width="6"/>
  </svg>

  <h1 class="sign__message">
    <span class="sign__line sign__line--first">The Good Lord does <span class="sign__emphasis">ALL</span> the healing...</span>
    <span class="sign__line sign__line--second">But we <span class="sign__emphasis">DO</span> collect the co-pay</span>
  </h1>

  <div class="brand">
    <span class="brand__name">Kinsella</span>
    <span class="brand__descriptor">Orthopedic Clinic</span>
  </div>
</main>
</body>
</html>
```